Business Cards for new orthopaedic surgery practice

My husband and I are starting our own orthopaedic surgery practice. We are looking for a business card that is uniform, but one will have my name/title and the other will have his. You can just create one design with my name on it for now. But when I choose your design as the winning design I will ask that you add another copy with his name/title.

We are looking for classy, simple, elite all in one. We like dark blues/a little gold/yellow. Something that goes with our logo. We want our logo incorporated. Here is all the info you need:
Business name: RV Spine & Vitality Center
Location: 38915 North Bramble Ave
Palm Hollow, FL 33990
Phone: 954-218-4630
Fax: 954-571-2846
Email: info@myrvspine.example

Names: Lucinda Ferrow, M.D.
Board Certified Hand and Upper Extremity Surgeon

Emeka Dlunga, M.D.
Board Certified Hip & Knee Replacement/General Orthopaedic Surgeon

Can decide what you want to put on the back. Maybe a slogan:
Rooted in Care. Focused on You

I am just going to upload our logo. The only thing is if we select you as the winning design, the location, and phone numbers may change. We will need your help to update that once fully solidified.

Industry/Entity Type

Medical

Contact Information for Business Card

Colors
0054AA
0677BA
7BADD7
CADEEF
E8F1F8
0094D4
00A9DD
6FCCEA
C7EBF8
E9F6FB

Requirements
Must have
• class, appeal,
Should not have
• We want to air on the side of masculine if we are looking at masculine vs. feminine feel. But we still want it classy, sophisticated, and something we will love

```html
<!DOCTYPE html>
<html lang="en">
<head>
<meta charset="utf-8">
<title>RV Spine &amp; Vitality Center – Business Card</title>
<link href="https://fonts.googleapis.com/css2?family=Jost:wght@400;500&family=Playfair+Display:wght@600&display=swap" rel="stylesheet">
<style>
  :root {
    --navy: #233468;
    --gold: #d8b25a;
    --paper: #ffffff;
    --backdrop: #bdbec0;
    --on-navy: #f3f1ea;
  }
  * { box-sizing: border-box; margin: 0; padding: 0; }
  html, body { width: 1200px; height: 900px; overflow: hidden; }
  body {
    background: var(--backdrop);
    font-family: "Jost", sans-serif;
    display: flex;
    align-items: center;
    justify-content: center;
    gap: 70px;
  }
  .card { position: relative; border-radius: 3px; }
  .card--front { width: 540px; height: 309px; background: var(--paper); color: var(--navy); }
  .card--back { width: 309px; height: 540px; background: var(--navy); color: var(--on-navy); }

  .doctor { position: absolute; left: 38px; top: 34px; }
  .doctor__name {
    font-family: "Playfair Display", serif;
    font-weight: 600;
    font-size: 23px;
    color: var(--gold);
    letter-spacing: 0.2px;
  }
  .doctor__title { font-size: 13.5px; line-height: 1.3; margin-top: 4px; letter-spacing: 0.4px; }
  .doctor__rule { width: 18px; height: 2px; background: var(--gold); margin-top: 22px; }

  .contact { position: absolute; left: 38px; top: 176px; list-style: none; }
  .contact li { display: flex; align-items: center; gap: 8px; font-size: 13px; line-height: 1.55; letter-spacing: 0.4px; }
  .contact svg { width: 11px; height: 11px; flex: none; }

  .brand {
    position: absolute;
    display: flex;
    align-items: center;
    gap: 10px;
    font-weight: 500;
    letter-spacing: 1.6px;
    text-transform: uppercase;
    line-height: 1.35;
  }
  .brand__dot { border-radius: 50%; flex: none; }
  .card--front .brand { right: 36px; top: 128px; width: 190px; font-size: 13px; color: var(--navy); }
  .card--front .brand__dot { width: 14px; height: 14px; background: var(--navy); }

  .address { position: absolute; right: 36px; bottom: 30px; display: flex; gap: 8px; font-size: 12.5px; line-height: 1.4; letter-spacing: 0.4px; }
  .address svg { width: 10px; height: 13px; margin-top: 2px; flex: none; }

  .card--back .brand { left: 50%; top: 150px; transform: translateX(-50%); width: 210px; font-size: 15px; color: var(--on-navy); }
  .card--back .brand__dot { width: 16px; height: 16px; background: var(--gold); }

  .social { position: absolute; left: 50%; top: 378px; transform: translateX(-50%); display: flex; align-items: center; gap: 10px; }
  .social__line { width: 70px; height: 1px; background: var(--on-navy); opacity: 0.8; }
  .social__spot { width: 15px; height: 15px; border-radius: 50%; background: var(--gold); }
  .slogan { position: absolute; left: 0; right: 0; top: 412px; text-align: center; font-size: 14px; letter-spacing: 1.6px; line-height: 1.45; }
</style>
</head>
<body>
  <section class="card card--front">
    <div class="doctor">
      <h1 class="doctor__name">Lucinda Ferrow, M.D.</h1>
      <p class="doctor__title">Board Certified Hand and<br>Upper Extremity Surgeon</p>
      <div class="doctor__rule"></div>
    </div>
    <ul class="contact">
      <li><svg viewBox="0 0 12 12"><path fill="var(--gold)" d="M2.4 0.6l2 2-1 1.4c.8 1.6 2 2.8 3.6 3.6l1.4-1 2 2-1.3 1.9C5.2 10.2 1.8 6.8 0.5 2z"/></svg>954-218-4630</li>
      <li><svg viewBox="0 0 12 12"><rect x="1" y="4" width="10" height="7" fill="var(--gold)"/><rect x="3" y="1" width="6" height="3" fill="var(--gold)"/></svg>954-571-2846</li>
      <li><svg viewBox="0 0 12 12"><circle cx="6" cy="6" r="5" fill="none" stroke="var(--gold)" stroke-width="1.4"/><path d="M1 6h10M6 1c-2.5 3-2.5 7 0 10M6 1c2.5 3 2.5 7 0 10" fill="none" stroke="var(--gold)" stroke-width="1"/></svg>info@myrvspine.example</li>
    </ul>
    <div class="brand"><span class="brand__dot"></span><span>RV Spine &amp; Vitality Center</span></div>
    <div class="address">
      <svg viewBox="0 0 10 13"><path fill="var(--gold)" d="M5 0C2.2 0 0 2.1 0 4.8 0 8.2 5 13 5 13s5-4.8 5-8.2C10 2.1 7.8 0 5 0zm0 6.6a1.8 1.8 0 1 1 0-3.6 1.8 1.8 0 0 1 0 3.6z"/></svg>
      <p>38915 North Bramble Ave<br>Palm Hollow, FL 33990</p>
    </div>
  </section>

  <section class="card card--back">
    <div class="brand"><span class="brand__dot"></span><span>RV Spine &amp; Vitality Center</span></div>
    <div class="social">
      <span class="social__line"></span>
      <span class="social__spot"></span>
      <span class="social__spot"></span>
      <span class="social__line"></span>
    </div>
    <p class="slogan">Grounded in Care.<br>Centered on You.</p>
  </section>
</body>
</html>
```